Silver Harbor Dental

I need a business card design for a state of the art and very modern dental practice. We provide general and pediatric dental services. I have attached a black and white EPS file of our logo, s logo design is not required. I have also attached two colors for our background and font. It does not have to be these two colors only. I am open to any suggestions. I have also included our current business card.
Things that should be different from our current business card is the logo, the website now is "www.silverhdental.com".
On the top right, where it says "like us on friendloop", now should say "Download our app on tap bazaar and vexa shelf store", but instead of our app, it should show the icon of our app, instead of tap bazaar and vexa shelf, it should show their icons, and not spell the words out.
I have also attached what the front of the card should more or less look like. It is the one with the different size fonts. I need the icon for phone, email, address, etc next to each. It is the file name "back of the businesscard1".

Target Market(s)

18-35 year-olds

Industry/Entity Type

Dental

Requirements
Nice to have
• the icon of our app, ormlist, and vexa shelf on the top right.

```html
<!DOCTYPE html>
<html lang="en">
<head>
<meta charset="utf-8">
<title>Silver Harbor Dental – Business Card</title>
<link rel="stylesheet" href="https://fonts.googleapis.com/css2?family=Lato:wght@400;700&display=swap">
<style>
  :root {
    --backdrop: #2b2b2d;
    --ink: #1f6a97;
    --ink-soft: #3d86ad;
    --teal: #5eaac4;
    --teal-deep: #8fc3d6;
    --paper: #ffffff;
    --mist: #e6f2f7;
  }
  * { margin: 0; padding: 0; box-sizing: border-box; }
  html, body {
    width: 1200px; height: 900px; overflow: hidden;
    background: var(--backdrop);
    font-family: "Lato", sans-serif;
    color: var(--ink);
  }
  .canvas {
    position: relative; width: 1200px; height: 900px;
    display: flex; flex-direction: column; align-items: center; justify-content: center; gap: 36px;
  }
  .card {
    position: relative; width: 700px; height: 400px; border-radius: 30px; overflow: hidden;
    background: linear-gradient(180deg, var(--mist) 0%, var(--paper) 40%, #e3f0f5 75%, var(--teal-deep) 100%);
  }
  .card svg.swoosh { position: absolute; inset: 0; width: 100%; height: 100%; }
  .card > div, .card > p { position: absolute; }

  .brand { display: flex; align-items: center; gap: 12px; }
  .brand-mark { width: 34px; height: 34px; border-radius: 50%; border: 2px solid var(--ink); flex: none; }
  .brand-name { font-size: 22px; font-weight: 400; letter-spacing: 1px; text-transform: uppercase; line-height: 1; }
  .brand-sub { font-size: 15px; color: var(--ink); margin-top: 4px; }

  /* front */
  .front .brand { left: 48px; top: 106px; }
  .download { right: 44px; top: 36px; display: flex; align-items: center; gap: 8px; font-size: 14px; }
  .app-icon { width: 46px; height: 46px; border-radius: 10px; background: linear-gradient(180deg, #5fb6d6, #1f86b3); }
  .store { font-size: 15px; font-weight: 700; }
  .person { left: 60px; top: 228px; }
  .person-name { font-size: 25px; font-weight: 700; padding-bottom: 6px; border-bottom: 1.5px solid var(--ink); width: 300px; }
  .contact { margin-top: 10px; font-size: 19px; line-height: 1.3; display: grid; grid-template-columns: 70px auto; }
  .address { right: 48px; top: 210px; text-align: right; font-size: 19px; line-height: 1.3; }

  /* back */
  .back .brand { right: 48px; top: 36px; }
  .back .brand-name { font-size: 17px; }
  .back .brand-sub { font-size: 12px; }
  .appointment { left: 60px; top: 150px; font-size: 20px; }
  .fields { left: 80px; top: 190px; width: 540px; font-size: 20px; }
  .field { display: flex; align-items: flex-end; gap: 14px; height: 32px; }
  .field-line { flex: 1; border-bottom: 1px solid var(--ink-soft); margin-bottom: 6px; }
  .notice { left: 80px; top: 300px; width: 560px; font-size: 19px; line-height: 1.35; }
</style>
</head>
<body>
<main class="canvas">

  <section class="card front" aria-label="Business card front">
    <svg class="swoosh" viewBox="0 0 700 400" preserveAspectRatio="none" aria-hidden="true">
      <path d="M0 210 C 220 175, 450 130, 700 140 L700 400 L0 400 Z" fill="#dcecf3" opacity="0.55"/>
      <path d="M0 210 C 220 175, 450 130, 700 140 L700 152 C 450 145, 220 190, 0 224 Z" fill="#ffffff"/>
      <line x1="370" y1="200" x2="655" y2="200" stroke="#1f6a97" stroke-width="1.2"/>
    </svg>

    <div class="download">
      <span>Download</span>
      <span class="app-icon" aria-label="Silver Harbor Dental app"></span>
      <span>on</span>
      <span class="store">ormlist</span>
      <span>&amp;</span>
      <span class="store">vexa shelf</span>
    </div>

    <div class="brand">
      <span class="brand-mark"></span>
      <div>
        <p class="brand-name">Silver Harbor Dental</p>
        <p class="brand-sub">General &amp; Pediatric Dentistry</p>
      </div>
    </div>

    <div class="person">
      <p class="person-name">Morgan Ellery DDS</p>
      <div class="contact">
        <span>Phone</span><span>(555) 310-4427</span>
        <span>Cell</span><span>(555) 862-0193</span>
        <span>Email</span><span>mellery@silverhdental.com</span>
      </div>
    </div>

    <div class="address">
      <p>482 Larkmoor Avenue</p>
      <p>Eastbrook, NY, 10472</p>
      <p>www.silverhdental.com</p>
    </div>
  </section>

  <section class="card back" aria-label="Business card back">
    <svg class="swoosh" viewBox="0 0 700 400" preserveAspectRatio="none" aria-hidden="true">
      <path d="M0 0 L700 0 L700 95 C 450 105, 200 110, 0 130 Z" fill="#e3f0f5"/>
      <path d="M0 130 C 200 110, 450 105, 700 95 L700 102 C 450 112, 200 118, 0 138 Z" fill="#c7e1ec"/>
    </svg>

    <div class="brand">
      <span class="brand-mark"></span>
      <div>
        <p class="brand-name">Silver Harbor Dental</p>
        <p class="brand-sub">General &amp; Pediatric Dentistry</p>
      </div>
    </div>

    <p class="appointment">Appointment</p>
    <div class="fields">
      <div class="field"><span>Name</span><span class="field-line"></span></div>
      <div class="field"><span>Date</span><span class="field-line"></span></div>
      <div class="field"><span>Time</span><span class="field-line"></span></div>
    </div>
    <p class="notice">If you are unable to keep your appointment, please notify us as soon as possible.</p>
  </section>

</main>
</body>
</html>
```